Homemaking training schools needs a Business Card design

Designer, Hello!

No special requirements, good-looking enough.
--------------------------------------------------------------------------

Name: Marcus Dale
Chairman
Tel: 0574-31759426
Mobile: 13817450926
Email: brimwell@mailtor.com
Web: www.kvd2018.com
Add: No.382, QinglanJie, BaolinQu, Ningbo, Zhejiang

LOGO
Ningbo KVD Homemaking Training School

Target Market(s)

pregnant women, mothers, infants, the elderly and families, including cleaning, cooking, nursing training.

Industry/Entity Type

Business

Contact Information for Business Card

Name: Marcus Dale
Chairman
Tel: 0574-31759426
Mobile: 13817450926
Email: brimwell@mailtor.com
Web: www.kvd2018.com

LOGO

Font styles to use
Serif
Sans Serif
Decorative

Requirements
Nice to have
• Feels: clean, specifications, safety, comfort, warmth and happiness.

```html
<!DOCTYPE html>
<html lang="en">
<head>
<meta charset="utf-8">
<title>KaiVenDa Business Card</title>
<link href="https://fonts.googleapis.com/css2?family=Arimo:wght@400;700&display=swap" rel="stylesheet">
<style>
  :root {
    --page-bg: #e6e3de;
    --brand-blue: #1f74bb;
    --brand-pink: #e5148a;
    --card-white: #ffffff;
    --card-grey: #e4e4e6;
    --text-white: #ffffff;
    --text-grey: #6d6d72;
  }
  * { box-sizing: border-box; margin: 0; padding: 0; }
  html, body {
    width: 1200px; height: 950px; overflow: hidden;
    background: var(--page-bg);
    font-family: "Arimo", Arial, sans-serif;
  }
  .sheet { position: relative; width: 1200px; height: 950px; }
  .card {
    position: absolute; left: 220px;
    width: 760px; height: 434px;
    border-radius: 4px; overflow: hidden;
    box-shadow: 0 8px 24px rgba(0,0,0,0.18);
  }
  /* Back side */
  .card-back {
    top: 26px;
    background: linear-gradient(135deg, var(--card-white) 35%, var(--card-grey) 100%);
    display: flex; flex-direction: column; align-items: center; justify-content: center;
  }
  .back-name {
    font-size: 48px; font-weight: 700; color: var(--brand-blue);
  }
  .back-web {
    margin-top: 40px;
    font-size: 19px; letter-spacing: 4px; color: var(--text-grey);
  }
  /* Front side */
  .card-front { top: 490px; background: var(--brand-blue); }
  .front-shape { position: absolute; inset: 0; width: 760px; height: 434px; }
  .contact {
    position: absolute; left: 44px; top: 34px;
    color: var(--text-white);
  }
  .contact-name { font-size: 26px; font-weight: 700; letter-spacing: 0.5px; }
  .contact-title { font-size: 15px; margin-top: 2px; }
  .contact-address { margin-top: 48px; font-size: 16px; line-height: 1.3; }
  .contact-list {
    list-style: none; margin-top: 8px; font-size: 16px; line-height: 1.45;
  }
  .contact-list li { display: flex; align-items: center; gap: 8px; }
  .contact-list svg { width: 14px; height: 14px; flex: none; }
  .front-name {
    position: absolute; left: 440px; top: 190px; width: 290px;
    text-align: center;
    font-size: 36px; font-weight: 700; color: var(--brand-blue);
  }
</style>
</head>
<body>
<main class="sheet">
  <section class="card card-back" aria-label="Card back">
    <p class="back-name">KaiVenDa</p>
    <p class="back-web">www.kvd2018.com</p>
  </section>

  <section class="card card-front" aria-label="Card front">
    <svg class="front-shape" viewBox="0 0 760 434" aria-hidden="true">
      <defs>
        <linearGradient id="whiteSweep" x1="0" y1="0" x2="1" y2="1">
          <stop offset="0.3" stop-color="#ffffff"/>
          <stop offset="1" stop-color="#e2e2e4"/>
        </linearGradient>
      </defs>
      <path d="M470 0 C380 110 350 300 410 434 L392 434 C332 300 356 110 440 0 Z" fill="#5a9ad0"/>
      <path d="M480 0 C380 110 350 300 410 434 L398 434 C334 300 360 110 452 0 Z" fill="var(--brand-pink)"/>
      <path d="M500 0 C400 110 372 300 420 434 L760 434 L760 0 Z" fill="url(#whiteSweep)"/>
    </svg>

    <div class="contact">
      <h1 class="contact-name">Marcus Dale</h1>
      <p class="contact-title">Chairman</p>
      <p class="contact-address">No.382, QinglanJie<br>BaolinQu<br>Ningbo, Zhejiang</p>
      <ul class="contact-list">
        <li>
          <svg viewBox="0 0 16 16" aria-hidden="true"><path fill="#fff" d="M2 5c0-2 2-3 6-3s6 1 6 3v1h-3V5H5v1H2zM4 7h8l2 7H2z"/><circle cx="8" cy="10.5" r="1.6" fill="#1f74bb"/></svg>
          0574-31759426
        </li>
        <li>
          <svg viewBox="0 0 16 16" aria-hidden="true"><rect x="4" y="1" width="8" height="14" rx="1.5" fill="#fff"/><rect x="5.5" y="3" width="5" height="8" fill="#1f74bb"/></svg>
          13817450926
        </li>
        <li>
          <svg viewBox="0 0 16 16" aria-hidden="true"><rect x="1" y="3" width="14" height="10" rx="1" fill="#fff"/><path d="M1.5 3.5 8 9l6.5-5.5" stroke="#1f74bb" stroke-width="1.3" fill="none"/></svg>
          brimwell@mailtor.com
        </li>
        <li>
          <svg viewBox="0 0 16 16" aria-hidden="true"><circle cx="8" cy="8" r="7" fill="#fff"/><path d="M1 8h14M8 1c-3 3-3 11 0 14M8 1c3 3 3 11 0 14" stroke="#1f74bb" stroke-width="1" fill="none"/></svg>
          www.kvd2018.com
        </li>
      </ul>
    </div>

    <p class="front-name">KaiVenDa</p>
  </section>
</main>
</body>
</html>
```